Alternative Health business needs a self help book cover design

Pale Brook Healing requires an E book and print cover design for a new self help book titled "Making The Bright Choice". Sub title 'Ways to build the glad days YOU seek' . Author Dorinda Crastley. The book is about deliberately changing things now, so you feel happy now and this then flows out an effects everything else in your life. It combines NLP, yoga philosophy and modern psychology in a down to earth, easy to read manner. I would like the cover to be happy, colourful, beautiful, artistic and hip. Maybe something hand drawn or painted. Something a woman would want to display and something that makes you smile and feel happy.
I don't want it to look like a romance novel and would prefer no photos of people. Pics are of other peoples covers I like. Thank you in advance. dorinda

Target Market(s)

woman 18-50

Industry/Entity Type

Business

Requirements
Must have
• happy feeling. professional look
Nice to have
• original drawing or painting
Should not have
• photos of real people, yellow smiley faces, sunsets, butterflies, yoga, tree, elements of my business logo

```html
<!DOCTYPE html>
<html lang="en">
<head>
<meta charset="utf-8">
<title>Making The Bright Choice – Cover Wrap</title>
<link rel="stylesheet" href="https://fonts.googleapis.com/css2?family=Cinzel:wght@400;500&family=Cormorant+Garamond:ital,wght@1,400&family=Raleway:wght@300;400&family=Arimo&display=swap">
<style>
  :root {
    --sky-teal: #6fa598;
    --sky-deep: #507f78;
    --haze: #a6bfa6;
    --meadow-pale: #c8c7a0;
    --field-gold: #c9a862;
    --field-rose: #b98a72;
    --mauve: #7a5670;
    --corner-plum: rgba(74, 51, 80, 0.6);
    --panel-white: rgba(255, 255, 255, 0.62);
    --title-blue: #1f3fa6;
    --ink: #111111;
    --light: #ffffff;
  }
  * { margin: 0; padding: 0; box-sizing: border-box; }
  html, body { width: 1200px; height: 831px; overflow: hidden; background: #ffffff; }

  .cover-wrap {
    position: relative;
    width: 1200px;
    height: 831px;
    overflow: hidden;
  }

  .backdrop-art {
    position: absolute;
    inset: 0;
    background:
      radial-gradient(ellipse 40% 35% at 100% 0%, var(--corner-plum), transparent 70%),
      radial-gradient(ellipse 30% 25% at 0% 0%, rgba(80,100,95,0.5), transparent 70%),
      linear-gradient(180deg,
        var(--sky-deep) 0%,
        var(--sky-teal) 28%,
        var(--haze) 52%,
        var(--meadow-pale) 64%,
        var(--field-gold) 76%,
        var(--field-rose) 88%,
        var(--mauve) 100%);
  }

  .heart-art {
    position: absolute;
    left: 39px;
    top: 154px;
    width: 506px;
    height: 500px;
    border-radius: 50%;
    background: radial-gradient(ellipse at center, transparent 38%, rgba(224,110,100,0.35) 55%, rgba(238,210,150,0.3) 68%, transparent 78%);
  }

  /* Back cover */
  .back-cover { position: absolute; left: 0; top: 0; width: 519px; height: 831px; }
  .blurb-panel {
    position: absolute;
    left: 32px;
    top: 100px;
    width: 487px;
    height: 760px;
    border-radius: 20px;
    background: var(--panel-white);
    padding: 18px 28px 0 27px;
  }
  .blurb-panel p {
    font-family: "Arimo", Arial, sans-serif;
    font-size: 12.2px;
    line-height: 1.27;
    color: var(--ink);
    text-align: justify;
    text-indent: 36px;
  }

  /* Spine */
  .spine { position: absolute; left: 519px; top: 0; width: 109px; height: 831px; }
  .spine-title {
    position: absolute;
    left: 58px;
    top: 26px;
    transform-origin: 0 0;
    transform: rotate(90deg);
    white-space: nowrap;
    font-family: "Cinzel", Georgia, serif;
    font-size: 33px;
    letter-spacing: 0.5px;
    color: var(--ink);
  }
  .spine-author {
    position: absolute;
    left: 75px;
    top: 590px;
    transform-origin: 0 0;
    transform: rotate(90deg);
    white-space: nowrap;
    font-family: "Raleway", Arial, sans-serif;
    font-size: 15px;
    color: var(--light);
  }

  /* Front cover */
  .front-cover { position: absolute; left: 628px; top: 0; width: 572px; height: 831px; text-align: center; }
  .front-author {
    position: absolute;
    left: 0; right: 0;
    top: 68px;
    padding-left: 14px;
    font-family: "Raleway", Arial, sans-serif;
    font-weight: 300;
    font-size: 26px;
    letter-spacing: 7px;
    color: var(--light);
  }
  .front-title {
    position: absolute;
    left: 40px; right: 0;
    top: 344px;
    font-family: "Cinzel", Georgia, serif;
    font-weight: 500;
    font-size: 38px;
    line-height: 60px;
    color: var(--title-blue);
  }
  .front-title .line { display: block; }
  .front-subtitle {
    position: absolute;
    left: 0; right: 0;
    top: 662px;
    font-family: "Cormorant Garamond", Georgia, serif;
    font-style: italic;
    font-size: 42px;
    line-height: 1.4;
    color: var(--light);
  }
</style>
</head>
<body>
<div class="cover-wrap">
  <div class="backdrop-art" role="img" aria-label="Soft painted texture in teal, pale cream and golden rose tones"></div>

  <section class="back-cover">
    <div class="blurb-panel">
      <p>Lorem ipsum dolor sit amet, consectetur adipiscing elit, sed do eiusmod tempor incididunt ut labore et dolore magna aliqua. Ut enim ad minim veniam, quis nostrud exercitation ullamco laboris nisi ut aliquip ex ea commodo consequat. Duis aute irure dolor in reprehenderit in voluptate velit esse cillum dolore eu fugiat nulla pariatur. Excepteur sint occaecat cupidatat non proident, sunt in culpa qui officia deserunt mollit anim id est laborum.</p>
      <p>Lorem ipsum dolor sit amet, consectetur adipiscing elit, sed do eiusmod tempor incididunt ut labore et dolore magna aliqua. Ut enim ad minim veniam, quis nostrud exercitation ullamco laboris nisi ut aliquip ex ea commodo consequat. Duis aute irure dolor in reprehenderit in voluptate velit esse cillum dolore eu fugiat nulla pariatur. Excepteur sint occaecat cupidatat non proident, sunt in culpa qui officia deserunt mollit anim id est laborum.</p>
      <p>Lorem ipsum dolor sit amet, consectetur adipiscing elit, sed do eiusmod tempor incididunt ut labore et dolore magna aliqua. Ut enim ad minim veniam, quis nostrud exercitation ullamco laboris nisi ut aliquip ex ea commodo consequat. Duis aute irure dolor in reprehenderit in voluptate velit esse cillum dolore eu fugiat nulla pariatur. Excepteur sint occaecat cupidatat non proident, sunt in culpa qui officia deserunt mollit anim id est laborum.</p>
    </div>
  </section>

  <section class="spine">
    <div class="spine-title">MAKING THE BRIGHT CHOICE</div>
    <div class="spine-author">DORINDA CRASTLEY</div>
  </section>

  <section class="front-cover">
    <div class="heart-art" role="img" aria-label="Illustrated ring of colourful winged insects arranged in a heart shape"></div>
    <div class="front-author">DORINDA CRASTLEY</div>
    <h1 class="front-title">
      <span class="line">MAKING THE</span>
      <span class="line">BRIGHT CHOICE</span>
    </h1>
    <p class="front-subtitle">Ways to build the glad days<br>YOU seek</p>
  </section>
</div>
</body>
</html>
```